Business card design for new, innovative company - BluePlinth

We are a new company looking for a business card design that is fun, different and quirky. Must use corporate colour green - CMYK C:55, M:0, Y:100, K:0, and corporate colour grey - C:0, M:0, Y: 0, K:70.

We have developed the first real time data application, in which people are able to profile the data of their existing customers in order to pull out more good fit clients to direct their marketing activities at.

Industry/Entity Type

Marketing

Requirements
Must have
• Logo, name, title, telephone number, fax number, email, website, address

```html
<!DOCTYPE html>
<html lang="en">
<head>
<meta charset="utf-8">
<title>BluePlinth business card</title>
<link rel="stylesheet" href="https://fonts.googleapis.com/css2?family=Nunito:wght@800&family=Open+Sans:wght@400;700&display=swap">
<style>
  :root {
    --brand-green: #6fbf3c;
    --brand-grey: #5c5d5f;
    --ink: #4a4a4a;
    --band: #ffffff;
    --stage-centre: #b4c2ca;
    --stage-edge: #8799a5;
    --card-glass: rgba(255, 255, 255, 0.22);
    --card-edge: rgba(255, 255, 255, 0.75);
  }
  * { box-sizing: border-box; margin: 0; padding: 0; }
  html, body { width: 1200px; height: 792px; overflow: hidden; }
  body {
    position: relative;
    background: radial-gradient(ellipse at 50% 45%, var(--stage-centre) 0%, var(--stage-edge) 100%);
    font-family: "Open Sans", Arial, sans-serif;
    color: var(--ink);
  }
  .card {
    position: absolute;
    top: 232px;
    width: 519px;
    height: 334px;
    border-radius: 18px;
    background: var(--card-glass);
    border: 1.5px solid var(--card-edge);
    overflow: hidden;
  }
  .card--front { left: 56px; }
  .card--back { left: 627px; }

  .card__top { position: absolute; inset: 0 0 auto 0; height: 172px; }
  .card__holder {
    position: absolute;
    top: 26px;
    right: 24px;
    font-size: 15px;
    color: var(--brand-grey);
  }
  .card__brand {
    position: absolute;
    top: 58px;
    left: 0;
    width: 100%;
    text-align: center;
    font-family: "Nunito", "Open Sans", sans-serif;
    font-weight: 800;
    font-size: 78px;
    letter-spacing: -1px;
    line-height: 1;
    color: var(--brand-green);
  }
  .card--back .card__top { transform: scaleX(-1); opacity: 0.42; }

  .card__band {
    position: absolute;
    left: 0;
    right: 0;
    top: 173px;
    height: 131px;
    background: var(--band);
    border-top: 4px solid var(--brand-green);
    border-bottom: 4px solid var(--brand-green);
  }

  .contact-list {
    list-style: none;
    padding: 11px 0 0 30px;
    font-size: 15.5px;
    line-height: 21px;
  }
  .contact-list li { display: flex; align-items: center; }
  .contact-list .icon { width: 16px; height: 16px; margin-right: 4px; flex: none; }
  .contact-list .indent { padding-left: 20px; }

  .website {
    text-align: center;
    padding-top: 38px;
    font-weight: 700;
    font-size: 24px;
    letter-spacing: 1px;
  }
  .website__lead { color: var(--brand-green); }
  .website__tail { color: var(--brand-grey); }
</style>
</head>
<body>

<section class="card card--front" aria-label="Card front">
  <div class="card__top">
    <p class="card__holder">Megan Carter</p>
    <p class="card__brand">BluePlinth</p>
  </div>
  <div class="card__band">
    <ul class="contact-list">
      <li>
        <svg class="icon" viewBox="0 0 16 16" aria-hidden="true"><rect x="4" y="1" width="8" height="14" rx="1.5" fill="none" stroke="var(--brand-green)" stroke-width="1.6"/><rect x="5.5" y="3" width="5" height="5" fill="var(--brand-green)"/><circle cx="8" cy="12" r="1" fill="var(--brand-green)"/></svg>
        07700900417
      </li>
      <li>
        <svg class="icon" viewBox="0 0 16 16" aria-hidden="true"><path d="M3.2 1.5l2.5 2.8-1.3 1.8c.9 2.2 2.5 3.8 4.7 4.8l1.8-1.3 2.8 2.5-1.7 2.2C6.9 14.1 1.8 9 1 3.1z" fill="var(--brand-green)"/></svg>
        01632 960482
      </li>
      <li>
        <svg class="icon" viewBox="0 0 16 16" aria-hidden="true"><path d="M1 6l7-4.5L15 6v8H1z" fill="var(--brand-green)"/><path d="M2 6.5l6 4 6-4" fill="none" stroke="#fff" stroke-width="1.2"/></svg>
        megan.carter@fenwaydistribution.com
      </li>
      <li>
        <svg class="icon" viewBox="0 0 16 16" aria-hidden="true"><path d="M8 1.5L0.8 8h2.2v6.5h3.8v-4h2.4v4h3.8V8h2.2z" fill="var(--brand-green)"/></svg>
        22 Fenway Court, Ely
      </li>
      <li class="indent">Cambridgeshire, CB7 4XZ</li>
    </ul>
  </div>
</section>

<section class="card card--back" aria-label="Card back">
  <div class="card__top" aria-hidden="true">
    <p class="card__holder">Megan Carter</p>
    <p class="card__brand">BluePlinth</p>
  </div>
  <div class="card__band">
    <p class="website"><span class="website__lead">www.blue</span><span class="website__tail">plinth.com</span></p>
  </div>
</section>

</body>
</html>
```